Elevator Pitch Workshop Flyer/Invitation

We need a flyer/announcement that will go in an email insert to our 3rd Year biosciences graduate students regarding a communications event we will be hosting. The event is a training and cocktail reception. We want to make it fun and exciting, yet also highlight that it will be a scientific communication training. The event is for third years Biosciences graduate students (they come from different science disciplines).

Flyer Details

Title: "Making your research make sense"

Short text: The ability to communicate clearly about your research will be critical for your future ability to get jobs and funding. This workshop will teach skills for refining what you want to say and how you say it. The focus will be the most challenging audience - the public - but tips you learn will translate to speaking to colleagues within your discipline or to a broader scientific audience. At the end you can put your skills to the test with a short video you can enter into a Biosciences-wide communication contest. Contest rules will be announced at the training.

Date Wednesday, June 11, 2014
Time: 3-5pm
Cocktail and Appetizer Reception Following
Location: TMRV Alder Hall 412C

Please RSVP Here

For any questions contact Marisol Dunleavy at mkdunleavy@halvercrest.edu

Poster image Idea: 1 person holding a cocktail asking another person, "So, what do you do?" The second person looks scared, or has a thought bubble with question marks or something else to indicate concern about how to answer the question.

We are open to creativity and other ideas!

Target Market(s)

Halvercrest Biosciences Graduate Students.

Industry/Entity Type

Communications

Requirements
Must have
• Title, Description,
Date, Time, Location,
Contact Info.

For 3rd Year Students

```html
<!DOCTYPE html>
<html lang="en">
<head>
<meta charset="utf-8">
<title>Halvercrest Biosciences – Communication Workshop</title>
<link rel="stylesheet" href="https://fonts.googleapis.com/css2?family=Ubuntu:wght@400;500;700&display=swap">
<style>
  :root {
    --stage: #e9e9e9;
    --red: #c4141c;
    --red-bright: #d81e25;
    --red-deep: #8b0b13;
    --white: #ffffff;
    --orange: #f7a20f;
    --orange-dark: #ec8400;
    --shirt-blue: #9fb6df;
    --shirt-pink: #e6bedb;
  }
  html, body {
    margin: 0;
    width: 1200px;
    height: 1200px;
    overflow: hidden;
    background: var(--stage);
  }
  .flyer {
    position: absolute;
    left: 160px;
    top: 31px;
    width: 662px;
    height: 856px;
    transform: scale(1.3293);
    transform-origin: top left;
    background: var(--red);
    font-family: "Ubuntu", sans-serif;
    overflow: hidden;
    box-shadow: 0 10px 30px rgba(0,0,0,.18);
  }
  .header {
    position: absolute;
    left: 0; top: 0;
    width: 662px; height: 145px;
    background: linear-gradient(180deg, #b70f17 0%, var(--red-bright) 45%, var(--red) 100%);
  }
  .header-stripe {
    position: absolute;
    left: 0; top: 14px;
    width: 380px; height: 12px;
    background: rgba(255,255,255,.06);
  }
  .brand-tab {
    position: absolute;
    right: 0; top: 0;
    width: 304px; height: 62px;
    background: var(--white);
    clip-path: polygon(0 0, 100% 0, 100% 100%, 32px 100%);
  }
  .brand {
    position: absolute;
    right: 30px; top: 21px;
    display: flex;
    align-items: center;
    gap: 8px;
    color: var(--red);
    font-weight: 500;
    font-size: 16px;
    letter-spacing: .3px;
    text-transform: uppercase;
  }
  .brand-dot {
    width: 8px; height: 8px;
    border-radius: 50%;
    background: var(--red);
  }
  .event-details {
    position: absolute;
    left: 35px; top: 30px;
    margin: 0;
    color: var(--white);
    font-weight: 500;
    font-size: 15.5px;
    line-height: 24px;
  }
  .rule {
    position: absolute;
    left: 0;
    width: 662px; height: 3px;
    background: var(--white);
  }
  .rule-top { top: 145px; }
  .rule-bottom { top: 378px; }
  .description {
    position: absolute;
    left: 0; top: 148px;
    width: 662px; height: 230px;
    background: var(--red-deep);
    display: flex;
    flex-direction: column;
    align-items: center;
    justify-content: center;
    color: var(--white);
    text-align: center;
  }
  .title {
    margin: 0 0 8px;
    font-size: 18px;
    font-weight: 700;
    line-height: 22px;
  }
  .summary {
    margin: 0;
    font-size: 11.6px;
    font-weight: 500;
    line-height: 17.5px;
  }
  .contact {
    margin: 8px 0 0;
    font-size: 11.6px;
    font-weight: 500;
    line-height: 17.5px;
  }
  .scene {
    position: absolute;
    left: 0; top: 381px;
    width: 662px; height: 475px;
    background: radial-gradient(ellipse at 60% 40%, #cf1a22 0%, var(--red) 55%, #a90d15 100%);
  }
  .person {
    position: absolute;
    z-index: 1;
  }
  .person-host {
    left: 0; top: 95px;
    width: 275px; height: 380px;
    background: linear-gradient(180deg, rgba(159,182,223,0) 0%, var(--shirt-blue) 40%, #dfe6f3 100%);
  }
  .person-guest {
    left: 390px; top: 185px;
    width: 235px; height: 290px;
    background: linear-gradient(180deg, rgba(230,190,219,0) 0%, var(--shirt-pink) 40%, #f3e4ef 100%);
  }
  .speech-bubble {
    position: absolute;
    left: 0; top: 0;
    z-index: 2;
  }
  .speech-text {
    position: absolute;
    z-index: 3;
    left: 172px; top: 107px;
    width: 340px;
    margin: 0;
    text-align: center;
    color: var(--white);
    font-weight: 700;
    font-size: 25px;
    line-height: 31px;
  }
</style>
</head>
<body>
  <article class="flyer">
    <header class="header">
      <div class="header-stripe"></div>
      <p class="event-details">Wednesday, June 11, 2014 3-5pm<br>with Cocktail and Appetizer<br>Reception Following...<br>TMRV Alder Hall 412C</p>
      <div class="brand-tab">
        <div class="brand"><span>Halvercrest Biosciences</span><span class="brand-dot"></span></div>
      </div>
    </header>
    <div class="rule rule-top"></div>
    <section class="description">
      <h1 class="title">Making your research make sense</h1>
      <p class="summary">The ability to communicate clearly about your research will be critical<br>for your future ability to get jobs and funding. This workshop will teach skills<br>for refining what you want to say and how you say it. The focus will be<br>the most challenging audience - the public - but tips you learn will translate<br>to speaking to colleagues within your discipline or to a broader scientific audience.<br>At the end you can put your skills to the test with a short video you can enter<br>into a Biosciences-wide communication contest. Contest rules<br>will be announced at the training.</p>
      <p class="contact">Please RSVP · Questions: Marisol Dunleavy, mkdunleavy@halvercrest.edu</p>
    </section>
    <div class="rule rule-bottom"></div>
    <section class="scene">
      <div class="person person-host" role="img" aria-label="Photo of a man in a blue shirt and tie holding a martini glass"></div>
      <div class="person person-guest" role="img" aria-label="Photo of a startled man in a pink shirt and tie raising his hands defensively"></div>
      <svg class="speech-bubble" width="662" height="475" viewBox="0 0 662 475" aria-hidden="true">
        <defs>
          <linearGradient id="bubble-fill" x1="0" y1="0" x2="0" y2="1">
            <stop offset="0" stop-color="#ef8a00"/>
            <stop offset="0.25" stop-color="#f7a20f"/>
            <stop offset="1" stop-color="#f9ab18"/>
          </linearGradient>
        </defs>
        <path d="M340 42 C440 42 512 88 512 142 C512 200 440 243 340 243 C325 243 312 242 300 240 L258 298 L268 230 C205 212 168 180 168 142 C168 88 240 42 340 42 Z"
              fill="url(#bubble-fill)" stroke="#ffffff" stroke-width="6" stroke-linejoin="round"/>
      </svg>
      <p class="speech-text">So,<br>what do you do?</p>
    </section>
  </article>
</body>
</html>
```